Flyer for a Business Consultant

I need a one-page description of services. I am a Brennick Certifed Talents Mentor. I do not have a personal website but think I will soon purchase this template https://varlowskins.example/skins/lectern/. I like the larger font, simplicity and larger font. I will attach his pricing flyer which I like - not to overly guide or restrict your creative thinking, but only to give a little perspective. I don't like busy, noisy - I like clarity, simplicity. Here 's the Brennick website which these same traits https://www.brennicktalentshub.example/ and can be a source of ideas and colors.

Target Market(s)

CEOs and Middle Managers in organizations

Industry/Entity Type

Financial Service

Colors

Designer to choose colors to be used in the design.

Requirements
Must have
• Clarity, simplicity, but also strength (not weak or frilly looking)
Nice to have
• Warm color(s), larger/not skinny font
Should not have
• Loud, noisy, busy

```html
<!DOCTYPE html>
<html lang="en">
<head>
<meta charset="utf-8">
<title>Talents Mentor Service Flyer</title>
<link rel="stylesheet" href="https://fonts.googleapis.com/css2?family=Dosis:wght@500;600;800&family=Nunito:wght@400;600;800;900&display=swap">
<style>
  :root {
    --green: #157a2c;
    --green-dark: #0f6a23;
    --ink: #1d1d1d;
    --charcoal: #3f3f3f;
    --overlay: rgba(70, 70, 70, 0.62);
    --paper: #ffffff;
    --backdrop: #b4b4b4;
  }
  * { margin: 0; padding: 0; box-sizing: border-box; }
  html, body { width: 1200px; height: 1200px; overflow: hidden; background: var(--backdrop); }
  .flyer {
    position: absolute; left: 189px; top: 20px;
    width: 990px; height: 1398px;
    transform: scale(0.83); transform-origin: top left;
    background: var(--paper);
    font-family: "Nunito", sans-serif; color: var(--ink);
    overflow: hidden;
  }
  .shape { position: absolute; }
  .frame-left { inset: 0; background: var(--green);
    clip-path: polygon(0 10px, 796px 10px, 612px 572px, 560px 572px, 551px 602px, 0 602px); }
  .frame-right { inset: 0; background: var(--green);
    clip-path: polygon(806px 10px, 990px 10px, 990px 572px, 630px 572px); }
  .photo-main { inset: 0;
    background: linear-gradient(100deg, #dcdcdc 0%, #d2d2cc 35%, #b7bf6a 48%, #e8e8e8 75%, #f1f1f1 100%);
    clip-path: polygon(0 59px, 727px 59px, 551px 602px, 0 602px); }
  .photo-side { inset: 0;
    background: linear-gradient(160deg, #eef0ee 0%, #cfd4d0 40%, #4a4f4a 70%, #e3e3e0 100%);
    clip-path: polygon(829px 59px, 990px 59px, 990px 527px, 677px 527px); }
  .title-panel { left: 0; top: 377px; width: 380px; height: 225px; background: var(--overlay); }
  .title {
    position: absolute; left: 49px; top: 392px;
    font-family: "Dosis", sans-serif; color: #fff; font-size: 44px; line-height: 49px;
  }
  .title .light { font-weight: 500; }
  .title .strong { font-weight: 800; }
  .tagline-band { inset: 0; background: var(--green);
    clip-path: polygon(0 602px, 558px 602px, 572px 642px, 0 642px); }
  .tagline { position: absolute; left: 49px; top: 608px; color: #fff; font-size: 22px; font-weight: 600; }
  .benefits { position: absolute; left: 49px; top: 672px; list-style: none; }
  .benefits li { color: var(--green); font-weight: 900; font-size: 19.5px; line-height: 36px; display: flex; align-items: center; gap: 11px; }
  .benefits svg { width: 13px; height: 13px; flex: none; }
  .service { position: absolute; left: 49px; width: 890px; }
  .service h2 {
    display: inline-block; background: var(--green); color: #fff;
    font-size: 23px; font-weight: 800; letter-spacing: 0.3px;
    padding: 3px 11px 4px 17px; margin-bottom: 10px;
  }
  .service p { font-size: 18.5px; line-height: 24px; text-align: justify; color: var(--ink); }
  .s-individual { top: 796px; }
  .s-workshop { top: 925px; }
  .s-follow { top: 1058px; }
  .s-follow h2 { margin-bottom: 14px; }
  .footer-left { inset: 0; background: var(--green);
    clip-path: polygon(0 1254px, 338px 1254px, 369px 1390px, 0 1390px); }
  .footer-right { inset: 0; background: var(--green);
    clip-path: polygon(679px 1254px, 990px 1254px, 990px 1390px, 649px 1390px); }
  .phone-bar { inset: 0; background: var(--charcoal);
    clip-path: polygon(364px 1317px, 656px 1317px, 649px 1390px, 372px 1390px); }
  .contacts { position: absolute; left: 34px; top: 1272px; color: #fff; font-size: 17px; }
  .contacts .row { display: flex; align-items: center; gap: 14px; height: 37px; }
  .contacts svg { width: 26px; height: 26px; flex: none; }
  .contacts b { font-weight: 800; }
  .follow { padding-left: 40px; gap: 10px !important; font-size: 16px; }
  .follow .net { display: inline-flex; align-items: center; gap: 5px; font-weight: 800; }
  .follow .dot { width: 12px; height: 12px; border-radius: 50%; background: #fff; }
  .coach { position: absolute; left: 364px; width: 290px; top: 1256px; text-align: center; }
  .coach-name { color: var(--green); font-size: 24px; font-weight: 900; letter-spacing: 0.3px; }
  .coach-role { font-size: 16px; font-weight: 600; margin-top: 2px; }
  .phone { position: absolute; left: 380px; top: 1328px; display: flex; align-items: center; gap: 10px;
    color: #fff; font-size: 32px; font-weight: 900; letter-spacing: 0.5px; }
  .phone svg { width: 26px; height: 26px; }
  .badge { position: absolute; left: 700px; top: 1290px; display: flex; align-items: center; gap: 17px; color: #fff; }
  .badge .mark { width: 52px; height: 67px; background: var(--charcoal); }
  .badge .kicker { font-size: 14px; letter-spacing: 0.5px; font-weight: 600; }
  .badge .name { font-size: 25px; font-weight: 600; line-height: 28px; }
</style>
</head>
<body>
<main class="flyer">
  <div class="shape frame-left"></div>
  <div class="shape frame-right"></div>
  <div class="shape photo-main" role="img" aria-label="Photo of a smiling coach speaking and gesturing in front of a light backdrop"></div>
  <div class="shape photo-side" role="img" aria-label="Photo of a professional on a phone call at an office desk"></div>
  <div class="shape title-panel"></div>
  <h1 class="title">
    <span class="light">A Strength-based</span><br>
    <span class="strong">Approach to</span><br>
    <span class="light">Managing Team</span><br>
    <span class="strong">Effectiveness</span>
  </h1>
  <div class="shape tagline-band"></div>
  <p class="tagline">We help teams grow stronger by</p>

  <ul class="benefits">
    <li><svg viewBox="0 0 12 12"><circle cx="6" cy="6" r="6" fill="#157a2c"/><path d="M3.2 6.3l1.8 1.8 3.8-4" stroke="#fff" stroke-width="1.6" fill="none"/></svg>Bringing a deep awareness of their strengths and the strengths of their associates.</li>
    <li><svg viewBox="0 0 12 12"><circle cx="6" cy="6" r="6" fill="#157a2c"/><path d="M3.2 6.3l1.8 1.8 3.8-4" stroke="#fff" stroke-width="1.6" fill="none"/></svg>Increasing the Team’s communication and sense of partnership.</li>
    <li><svg viewBox="0 0 12 12"><circle cx="6" cy="6" r="6" fill="#157a2c"/><path d="M3.2 6.3l1.8 1.8 3.8-4" stroke="#fff" stroke-width="1.6" fill="none"/></svg>Improving employee engagement and effectiveness.</li>
  </ul>

  <section class="service s-individual">
    <h2>Individual sessions</h2>
    <p style="text-align:left">Conversational feedback and coaching sessions based on Brennick’s TalentMap assessments. These sessions last about an hour and lead to a personalized<br>translation of the results and how their strengths show up in their work and inherent blind spots they bring.</p>
  </section>
  <section class="service s-workshop">
    <h2>Strength Discovery Workshop</h2>
    <p>A retreat-style Team Workshop in which the team learns each other’s unique Top 5 strengths. The session is very interactive and provides a common language that leads to improved communication and effectiveness. Tailored in 2.3.and 4-hour options are tailored to your Team’s challenges and opportunities.</p>
  </section>
  <section class="service s-follow">
    <h2>Follow-on modules</h2>
    <p>Follow-on is important to make the insights learned to be practical and integrated into the Teams’ approach and workflows.</p>
    <p style="text-align:left">In a debrief session included as part of the workshop, we provide several 15-minute exercise modules for use in regular meetings, and we offer guest facilitated modules of 30- 60 minutes each.</p>
  </section>

  <div class="shape footer-left"></div>
  <div class="shape footer-right"></div>
  <div class="shape phone-bar"></div>

  <div class="contacts">
    <div class="row"><svg viewBox="0 0 26 26"><circle cx="13" cy="13" r="12" fill="#fff"/><rect x="7" y="9" width="12" height="8.5" fill="none" stroke="#157a2c" stroke-width="1.5"/><path d="M7 9l6 5 6-5" fill="none" stroke="#157a2c" stroke-width="1.5"/></svg><span>dalton@<b>talentsIQ</b>.example</span></div>
    <div class="row"><svg viewBox="0 0 26 26"><circle cx="13" cy="13" r="11" fill="none" stroke="#fff" stroke-width="1.8"/><ellipse cx="13" cy="13" rx="5" ry="11" fill="none" stroke="#fff" stroke-width="1.5"/><path d="M2 13h22M4 8h18M4 18h18" stroke="#fff" stroke-width="1.3"/></svg><span>www.<b>brennicktalentshub</b>.example</span></div>
    <div class="row follow"><span>Fllow Us:</span><span class="net"><span class="dot"></span>Chirpline</span><span class="net"><span class="dot"></span>Streamly</span></div>
  </div>

  <div class="coach">
    <div class="coach-name">Dalton Merriweather</div>
    <div class="coach-role">Brennick Workplace Talents Mentor</div>
  </div>
  <div class="phone">
    <svg viewBox="0 0 26 26"><circle cx="13" cy="13" r="11.5" fill="none" stroke="#fff" stroke-width="1.8"/><path d="M9 7.5l2.2 2.6-1.3 1.6c.8 1.8 2.1 3.1 3.9 3.9l1.6-1.3 2.6 2.2-1.4 2c-4.4-.4-8.7-4.7-9.1-9.1z" fill="#fff"/></svg>
    <span>555-014-2290</span>
  </div>

  <div class="badge">
    <div class="mark"></div>
    <div>
      <div class="kicker">BRENNICK CERTIFIED</div>
      <div class="name">Talents Mentor</div>
    </div>
  </div>
</main>
</body>
</html>
```